Clinical psychologist - Psychotherapist business card

Hi everyone, I'm a clinical psychologist and psychotherapist, and I’m looking for a logo for my business card. The front will feature only the logo, while the back will include my contact details (and possibly a subtle touch of the logo). I've found two logos that I like, but the first one feels a bit childish—it lacks professionalism and doesn’t stand out from other similar designs. The second one, which I do like, unfortunately gives off a clinical, impersonal vibe.

Feel free to improvise—you don’t need to base the design on the logos I previously mentioned.

I generally prefer minimalistic designs that convey warmth, trust, and professionalism. I’d also like the card to have a bright background to make it feel inviting.

Additionally, I’m leaning toward using letterpress for the print technique, so the design should be compatible with that style—elegant, tactile, and clean. However, I’m still open to other options if they better suit the design.

UPDATE: I'm considering naming my business “Aurevan” (top-level domain: .gr), so you could incorporate that as well.

Target Market(s)

Psychology clients, Psychiatrists, Social media users

Industry/Entity Type

Clinical psychologist - Psychotherapist

Contact Information for Business Card

To be added later on

Colors

Designer to choose colors to be used in the design.

Requirements
Nice to have
• Possibly my initials on the front side. They are Δ Μ (capital letters) or δ μ (small letters).
Should not have
• Portraits of famous psychologists

```html
<!DOCTYPE html>
<html lang="en">
<head>
<meta charset="utf-8">
<title>Aurevan – Business Card</title>
<link href="https://fonts.googleapis.com/css2?family=Cinzel:wght@400;600;700&display=swap" rel="stylesheet">
<style>
  :root {
    --backdrop: #dcdddf;
    --card: #ffffff;
    --card-back: #f8f8f9;
    --navy: #1f3f7a;
    --red: #d8333a;
    --faint: #ecedf0;
  }
  * { box-sizing: border-box; margin: 0; padding: 0; }
  html, body { width: 1200px; height: 833px; overflow: hidden; }
  body {
    background: var(--backdrop);
    font-family: "Cinzel", serif;
    color: var(--navy);
    display: flex;
    align-items: center;
    justify-content: center;
    gap: 60px;
  }
  .card {
    position: relative;
    width: 520px;
    height: 320px;
    border-radius: 26px;
    background: var(--card);
    box-shadow: 0 0 0 3px var(--navy), 0 10px 24px rgba(0,0,0,.12);
    overflow: hidden;
  }
  /* Front */
  .card--front { display: flex; align-items: center; justify-content: center; }
  .brand { display: flex; align-items: center; gap: 16px; }
  .brand__dot { width: 14px; height: 14px; border-radius: 50%; background: var(--red); }
  .brand__name { font-size: 40px; font-weight: 400; letter-spacing: .14em; color: var(--navy); }

  /* Back */
  .card--back { background: var(--card-back); }
  .card__decor {
    position: absolute; right: -40px; top: 70px;
    width: 260px; height: 260px; border-radius: 50%;
    border: 2px solid var(--faint);
  }
  .back__brand { position: absolute; top: 36px; left: 0; right: 0; display: flex; justify-content: center; align-items: center; gap: 10px; }
  .back__brand .brand__dot { width: 8px; height: 8px; }
  .back__brand .brand__name { font-size: 20px; letter-spacing: .12em; }
  .holder { position: absolute; left: 40px; top: 118px; }
  .holder__name { font-size: 34px; font-weight: 700; letter-spacing: .02em; line-height: 1.2; }
  .holder__name span { font-weight: 400; }
  .holder__company { font-size: 11px; font-weight: 600; letter-spacing: .06em; margin-top: 2px; }
  .holder__company em { font-style: normal; color: var(--red); }
  .divider { position: absolute; left: 0; right: 0; top: 200px; height: 2px; background: var(--red); }
  .contacts { position: absolute; list-style: none; font-size: 10.5px; font-weight: 600; letter-spacing: .05em; }
  .contacts li { display: flex; align-items: center; gap: 10px; height: 22px; white-space: nowrap; }
  .contacts--left { left: 24px; top: 214px; }
  .contacts--right { right: 30px; top: 248px; }
  .icon { width: 14px; height: 14px; flex: none; }
</style>
</head>
<body>
  <section class="card card--front" aria-label="Card front">
    <div class="brand">
      <span class="brand__dot"></span>
      <span class="brand__name">AUREVAN</span>
    </div>
  </section>

  <section class="card card--back" aria-label="Card back">
    <div class="card__decor"></div>
    <div class="back__brand">
      <span class="brand__dot"></span>
      <span class="brand__name">AUREVAN</span>
    </div>
    <div class="holder">
      <p class="holder__name">YOUR <span>NAME</span></p>
      <p class="holder__company">COMPANY NAME : <em>AUREVAN</em></p>
    </div>
    <div class="divider"></div>
    <ul class="contacts contacts--left">
      <li>
        <svg class="icon" viewBox="0 0 14 14"><circle cx="7" cy="7" r="7" fill="#d8333a"/><path d="M5 3.5l1.2 1.6-.7.8c.4.9 1.1 1.6 2 2l.8-.7 1.6 1.2-.8 1.3C6.6 9.5 4.5 7.4 3.7 4.9z" fill="#fff"/></svg>
        123 456 789
      </li>
      <li>
        <svg class="icon" viewBox="0 0 14 14"><circle cx="7" cy="7" r="7" fill="#d8333a"/><circle cx="7" cy="7" r="3.6" fill="none" stroke="#fff" stroke-width="1"/><path d="M3.4 7h7.2M7 3.4c-1.6 2-1.6 5.2 0 7.2M7 3.4c1.6 2 1.6 5.2 0 7.2" fill="none" stroke="#fff" stroke-width=".8"/></svg>
        YOUR WEBSITE NAME HERE
      </li>
    </ul>
    <ul class="contacts contacts--right">
      <li>
        <svg class="icon" viewBox="0 0 14 14"><circle cx="7" cy="7" r="7" fill="#d8333a"/><rect x="3.8" y="4.8" width="6.4" height="4.4" fill="none" stroke="#fff" stroke-width=".9"/><path d="M3.8 4.8L7 7.4l3.2-2.6" fill="none" stroke="#fff" stroke-width=".9"/></svg>
        YOUR MAIL ADDRESS HERE
      </li>
      <li>
        <svg class="icon" viewBox="0 0 14 14"><circle cx="7" cy="7" r="7" fill="#d8333a"/><path d="M7 3.3a2.4 2.4 0 0 1 2.4 2.4C9.4 7.6 7 10.6 7 10.6S4.6 7.6 4.6 5.7A2.4 2.4 0 0 1 7 3.3z" fill="#fff"/><circle cx="7" cy="5.7" r=".9" fill="#d8333a"/></svg>
        YOUR STREET ADDRESS HERE
      </li>
    </ul>
  </section>
</body>
</html>
```